WHEAT PRODUCTS BAG DESIGN

• Bag dimensions: look at the picture »dimensions«. Picture represents dimensions for 1 kilogram bag.
• We are selling many products made from wheat. Those are: three types of white wheat flour, wheat wholegrain flour, half-withe wheat flour, black wheat flour and wheat porridge. Our main challenge is that we don’t know how to distinguish them through bag design, while design would still remain unified for all wheat products. We think that name of the wheat flour type on the bag just isn’t practical for our consumers who are buying in a hurry, when they for example rather pay attention to the bag colors than on what is written on the bag. Currently we use one design for all different kinds of flour which isn't very practical.
• I also uploaded design of an existing bag just in case you want to see it.

Colors

Designer to choose colors to be used in the design.

Requirements
Must have
• • We would like to integrate our logo (look at the picture »logo«) and weight of a product (1 kg) on the front side of a bag. And following information on the right or left side of a bag:
• Mlin Borovec d.o.o.
• Zelena pot 4c
• 8295 Podgorje pri Zidanem
• Slovenija
• tel.: 07 53 81 906
• www.zrnopek.com
Nice to have
• We do hope to get 7 variations of one designs (one for each wheat product).

```html
<!DOCTYPE html>
<html lang="en">
<head>
<meta charset="utf-8">
<title>Mlin Borovec – Flour Bags</title>
<link href="https://fonts.googleapis.com/css2?family=Anton&family=Marcellus&family=Open+Sans:wght@400;700&display=swap" rel="stylesheet">
<style>
:root{
  --bg:#ffffff;
  --cream:#f8ecdc;
  --white-label:#fffdf9;
  --orange:#e0601c;
  --orange-dark:#c9501a;
  --maroon:#7e2a24;
  --maroon-dark:#6a211c;
  --red:#c8102e;
  --yellow:#f3d22a;
  --ink:#3a2a22;
  --field:#c98a6c;
}
*{box-sizing:border-box;margin:0;padding:0}
html,body{width:1200px;height:1051px;overflow:hidden;background:var(--bg)}
body{position:relative;font-family:"Open Sans",sans-serif;color:var(--ink)}
.bag{position:absolute;top:125px;height:800px;display:flex}
.bag--white{left:80px;--accent:var(--orange);--accent-dark:var(--orange-dark)}
.bag--whole{left:650px;--accent:var(--maroon);--accent-dark:var(--maroon-dark)}
.panel{position:relative;height:100%;background:var(--cream);overflow:hidden}
.panel--side{width:150px;border-right:1px solid #ead6bf}
.panel--front{width:320px}
.pattern{position:absolute;left:0;top:0;right:0;height:420px;
  background:linear-gradient(180deg,#f5e3cc 0%,var(--cream) 100%)}
.landscape{position:absolute;left:0;right:0;top:430px;bottom:50px;
  background:linear-gradient(180deg,rgba(232,196,170,0) 0%,#e4b597 30%,var(--field) 70%,#b7765a 100%)}
.band{position:absolute;left:0;right:0;bottom:0;height:50px;background:var(--accent)}
.band-text{position:absolute;bottom:14px;font-size:7px;letter-spacing:.5px;color:#fbe6d6;text-transform:uppercase;white-space:nowrap}
.panel--side .band-text{font-size:5.5px;letter-spacing:0;left:8px}
.brand{position:absolute;left:0;right:0;top:250px;display:flex;align-items:center;justify-content:center;gap:8px}
.brand-dot{width:30px;height:30px;border-radius:50%;background:var(--yellow)}
.brand-name{font-weight:700;font-size:24px;color:var(--maroon)}
.panel--side .brand{top:240px;gap:5px}
.panel--side .brand-dot{width:22px;height:22px}
.panel--side .brand-name{font-size:18px}
.label{position:absolute;display:flex;flex-direction:column;align-items:stretch;
  background:linear-gradient(180deg,var(--white-label) 0%,var(--white-label) 55%,rgba(255,253,249,.55) 100%);
  border:1px solid var(--accent);outline:6px solid rgba(255,253,249,.9);text-align:center}
.panel--front .label{left:32px;width:256px;top:345px;height:400px;padding:18px 16px 28px}
.panel--side .label{left:12px;width:126px;top:330px;height:420px;padding:14px 8px 30px}
.title{font-family:"Anton",sans-serif;color:var(--accent);line-height:.98;text-transform:uppercase;letter-spacing:1px;font-weight:400}
.panel--front .title{font-size:62px}
.panel--front .title--three{font-size:45px}
.panel--side .title{font-size:38px}
.panel--side .title--three{font-size:30px}
.rule{height:2px;background:var(--accent);margin:8px 0 6px}
.kind{font-family:"Marcellus",serif;color:var(--ink)}
.panel--front .kind{font-size:32px}
.panel--side .kind{font-size:22px}
.copy{font-size:8px;line-height:1.35;margin:8px 6px 0}
.tag{align-self:center;margin-top:10px;width:180px;padding:5px 0;background:var(--accent);color:#fff;font-size:8.5px;font-weight:700}
.copy--small{font-size:6.5px;margin-top:10px}
.badges{display:flex;justify-content:center;gap:12px;margin-top:auto}
.badge{display:flex;flex-direction:column;align-items:center;gap:2px;font-size:5.5px;font-weight:700;color:var(--accent)}
.badge-icon{width:20px;height:20px}
.address{font-size:7px;line-height:1.4;margin-top:8px}
.contact{display:flex;justify-content:space-between;font-size:6px;font-weight:700;color:var(--accent);
  border-top:1px solid var(--accent);border-bottom:1px solid var(--accent);padding:3px 0;margin-top:10px}
.panel--side .copy{font-size:6px;margin-top:8px}
.panel--side .badges{gap:8px}
.weight{position:absolute;left:50%;bottom:0;width:28px;height:55px;margin-left:-14px;background:var(--red)}
.weight-disc{position:absolute;left:50%;bottom:28px;width:44px;height:44px;margin-left:-22px;border-radius:50%;
  background:var(--red);border:2px solid var(--yellow);color:#fff;font-size:12px;display:flex;align-items:center;justify-content:center}
.panel--side .weight{width:22px;height:50px;margin-left:-11px}
.panel--side .weight-disc{width:34px;height:34px;margin-left:-17px;bottom:24px;font-size:9px}
</style>
</head>
<body>

<section class="bag bag--white">
  <div class="panel panel--side">
    <div class="pattern" role="img" aria-label="Fine diamond line pattern"></div>
    <div class="landscape" role="img" aria-label="Engraved farm landscape with wheat field"></div>
    <div class="brand"><span class="brand-dot"></span><span class="brand-name">Borovec</span></div>
    <div class="label">
      <h2 class="title">White<br>Wheat</h2>
      <div class="rule"></div>
      <p class="kind">FLOUR</p>
      <p class="address">Mlin Borovec d.o.o.<br>Zelena pot 4c<br>8295 Podgorje pri Zidanem<br>Slovenija</p>
      <div class="contact"><span>www.zrnopek.com</span><span>tel.: 07 53 81 906</span></div>
      <p class="copy">Lorem Ipsum is simply dummy text of the printing and typesetting industry.</p>
      <div class="badges">
        <div class="badge"><svg class="badge-icon" viewBox="0 0 20 20"><circle cx="10" cy="10" r="9" fill="none" stroke="currentColor" stroke-width="1.6"/><path d="M5 5l10 10" stroke="currentColor" stroke-width="1.6"/></svg>NO GMO</div>
        <div class="badge"><svg class="badge-icon" viewBox="0 0 20 20"><circle cx="10" cy="10" r="9" fill="none" stroke="currentColor" stroke-width="1.6"/><path d="M6 6l4 8 4-8" fill="none" stroke="currentColor" stroke-width="1.6"/></svg>VEGAN</div>
      </div>
    </div>
    <div class="band"><span class="band-text">www.zrnopek.com</span></div>
    <div class="weight"></div><div class="weight-disc">1KG</div>
  </div>
  <div class="panel panel--front">
    <div class="pattern" role="img" aria-label="Fine diamond line pattern"></div>
    <div class="landscape" role="img" aria-label="Engraved farm landscape with tractor and wheat field"></div>
    <div class="brand"><span class="brand-dot"></span><span class="brand-name">Borovec</span></div>
    <div class="label">
      <h1 class="title">White<br>Wheat</h1>
      <div class="rule"></div>
      <p class="kind">FLOUR</p>
      <p class="copy">Lorem Ipsum is simply dummy text of the printing and typesetting industry.</p>
      <p class="tag">Lorem Ipsum is simply dummy text</p>
      <p class="copy copy--small">Lorem Ipsum is simply dummy text of the printing and typesetting industry.</p>
      <div class="badges">
        <div class="badge"><svg class="badge-icon" viewBox="0 0 20 20"><circle cx="10" cy="10" r="9" fill="none" stroke="currentColor" stroke-width="1.6"/><path d="M5 5l10 10" stroke="currentColor" stroke-width="1.6"/></svg>NO GMO</div>
        <div class="badge"><svg class="badge-icon" viewBox="0 0 20 20"><circle cx="10" cy="10" r="9" fill="none" stroke="currentColor" stroke-width="1.6"/><path d="M6 6l4 8 4-8" fill="none" stroke="currentColor" stroke-width="1.6"/></svg>VEGAN</div>
      </div>
    </div>
    <div class="band">
      <span class="band-text" style="left:12px">www.zrnopek.com</span>
      <span class="band-text" style="right:12px">Mlin Borovec d.o.o.</span>
    </div>
    <div class="weight"></div><div class="weight-disc">1KG</div>
  </div>
</section>

<section class="bag bag--whole">
  <div class="panel panel--side">
    <div class="pattern" role="img" aria-label="Fine diamond line pattern"></div>
    <div class="landscape" role="img" aria-label="Engraved farm landscape with wheat field"></div>
    <div class="brand"><span class="brand-dot"></span><span class="brand-name">Borovec</span></div>
    <div class="label">
      <h2 class="title title--three">Wheat<br>Whole<br>Grain</h2>
      <div class="rule"></div>
      <p class="kind">FLOUR</p>
      <p class="address">Mlin Borovec d.o.o.<br>Zelena pot 4c<br>8295 Podgorje pri Zidanem<br>Slovenija</p>
      <div class="contact"><span>www.zrnopek.com</span><span>tel.: 07 53 81 906</span></div>
      <p class="copy">Lorem Ipsum is simply dummy text of the printing and typesetting industry.</p>
      <div class="badges">
        <div class="badge"><svg class="badge-icon" viewBox="0 0 20 20"><circle cx="10" cy="10" r="9" fill="none" stroke="currentColor" stroke-width="1.6"/><path d="M5 5l10 10" stroke="currentColor" stroke-width="1.6"/></svg>NO GMO</div>
        <div class="badge"><svg class="badge-icon" viewBox="0 0 20 20"><circle cx="10" cy="10" r="9" fill="none" stroke="currentColor" stroke-width="1.6"/><path d="M6 6l4 8 4-8" fill="none" stroke="currentColor" stroke-width="1.6"/></svg>VEGAN</div>
      </div>
    </div>
    <div class="band"><span class="band-text">www.zrnopek.com</span></div>
    <div class="weight"></div><div class="weight-disc">1KG</div>
  </div>
  <div class="panel panel--front">
    <div class="pattern" role="img" aria-label="Fine diamond line pattern"></div>
    <div class="landscape" role="img" aria-label="Engraved farm landscape with tractor and wheat field"></div>
    <div class="brand"><span class="brand-dot"></span><span class="brand-name">Borovec</span></div>
    <div class="label">
      <h1 class="title title--three">Wheat<br>Whole<br>Grain</h1>
      <div class="rule"></div>
      <p class="kind">FLOUR</p>
      <p class="copy">Lorem Ipsum is simply dummy text of the printing and typesetting industry.</p>
      <p class="tag">Lorem Ipsum is simply dummy text</p>
      <p class="copy copy--small">Lorem Ipsum is simply dummy text of the printing and typesetting industry.</p>
      <div class="badges">
        <div class="badge"><svg class="badge-icon" viewBox="0 0 20 20"><circle cx="10" cy="10" r="9" fill="none" stroke="currentColor" stroke-width="1.6"/><path d="M5 5l10 10" stroke="currentColor" stroke-width="1.6"/></svg>NO GMO</div>
        <div class="badge"><svg class="badge-icon" viewBox="0 0 20 20"><circle cx="10" cy="10" r="9" fill="none" stroke="currentColor" stroke-width="1.6"/><path d="M6 6l4 8 4-8" fill="none" stroke="currentColor" stroke-width="1.6"/></svg>VEGAN</div>
      </div>
    </div>
    <div class="band">
      <span class="band-text" style="left:12px">www.zrnopek.com</span>
      <span class="band-text" style="right:12px">Mlin Borovec d.o.o.</span>
    </div>
    <div class="weight"></div><div class="weight-disc">1KG</div>
  </div>
</section>

</body>
</html>
```